DNN Website Design Project

We are going to recreate the website www.mivortalstudio.com. This is a DNN website. We like http://www.prunolabhq.com/ and something like http://www.quillharborworks.com/

Look at mivortalstudio.com to see what we do, SMM, SEO and website development mostly. We have a number of video testimonials and want people to be able to contact us easily and have social media integration.

Target Market(s)

small and medium sized business owners, doctors, private practice professionals, lawyers, service pros (plumbers, electricians)

Industry/Entity Type

Media

```html
<!DOCTYPE html>
<html lang="en">
<head>
<meta charset="utf-8">
<title>Mivortal Studio, Inc. — Web Design &amp; Support Services</title>
<link rel="stylesheet" href="https://fonts.googleapis.com/css2?family=Open+Sans:wght@400;600;700&family=Tinos:ital@0;1&family=Arimo:wght@400;700&display=swap">
<style>
  :root {
    --brand-red: #d00000;
    --accent-orange: #e8441a;
    --rule-grey: #c4c4c4;
    --text-dark: #222222;
    --text-mid: #555555;
    --text-soft: #8a8a8a;
    --page-bg: #f7f7f7;
    --white: #ffffff;
    --neutral-block: #d9d9d9;
  }
  * { margin: 0; padding: 0; box-sizing: border-box; }
  html, body { width: 1200px; height: 884px; overflow: hidden; }
  body {
    position: relative;
    background: var(--page-bg);
    font-family: "Arimo", Arial, sans-serif;
    color: var(--text-dark);
  }
  .abs { position: absolute; }

  .top-bar { left: 0; top: 0; width: 1200px; height: 4px; background: var(--brand-red); }

  /* Brand */
  .brand-mark { left: 30px; top: 25px; width: 82px; height: 82px; background: var(--neutral-block); }
  .brand-name { left: 122px; top: 27px; font-size: 15px; color: var(--text-dark); }
  .brand-tagline { left: 120px; top: 48px; width: 178px; font-size: 7px; font-weight: 700; line-height: 9px; text-align: center; color: var(--text-dark); }
  .brand-phone { left: 163px; top: 81px; font-size: 14px; letter-spacing: 0.5px; color: var(--text-dark); }

  /* Account links */
  .account-links { right: 30px; top: 16px; display: flex; gap: 16px; font-size: 12px; color: var(--text-mid); }
  .account-links span { display: flex; align-items: center; gap: 5px; }
  .account-links svg { width: 13px; height: 13px; }
  .cart-summary { right: 30px; top: 55px; font-size: 12px; color: var(--text-mid); }
  .cart-summary b { font-weight: 400; color: var(--accent-orange); }

  .follow-label { left: 795px; top: 85px; font-size: 12px; color: var(--text-dark); }
  .social-box { top: 83px; width: 18px; height: 18px; background: #7d7d7d; border-radius: 2px; }
  .search-field { left: 946px; top: 83px; width: 165px; height: 25px; border: 1px solid #d6d6d6; background: var(--white); font-size: 11px; color: #aaa; padding: 6px 6px; }
  .search-button { left: 1111px; top: 83px; width: 61px; height: 25px; background: var(--brand-red); color: var(--white); font-size: 12px; line-height: 25px; text-align: center; }

  /* Navigation */
  .nav-rule-top { left: 0; top: 121px; width: 1200px; height: 1px; background: #9a9a9a; }
  .nav-rule-bottom { left: 0; top: 169px; width: 1200px; height: 2px; background: var(--accent-orange); }
  .main-nav { left: 91px; top: 131px; display: flex; align-items: center; font-family: "Open Sans", Arial, sans-serif; font-size: 13px; color: #666; }
  .main-nav span { margin-right: 58px; }
  .main-nav .is-active { background: var(--brand-red); color: var(--white); font-weight: 600; padding: 6px 13px 7px; margin-right: 41px; }

  /* Hero */
  .hero-band { left: 16px; top: 204px; width: 1170px; height: 348px; background: radial-gradient(ellipse at 30% 45%, #e00000 0%, #c80000 55%, #a00000 100%); }
  .hero-kicker { left: 72px; top: 292px; font-family: "Open Sans", Arial, sans-serif; font-size: 27px; color: var(--white); letter-spacing: -0.5px; }
  .hero-headline { left: 70px; top: 309px; font-family: "Open Sans", Arial, sans-serif; font-weight: 700; font-size: 56px; color: var(--white); letter-spacing: -1px; }
  .hero-button { left: 79px; top: 410px; width: 223px; height: 41px; background: linear-gradient(#ffffff, #d9d9d9); color: #666; font-family: "Arimo", Arial, sans-serif; font-size: 19px; line-height: 41px; text-align: center; }
  .hero-devices { left: 590px; top: 183px; width: 586px; height: 377px; border-radius: 14px; background: linear-gradient(135deg, #2b2b2b 0%, #4a4a4a 30%, #e6e6e6 60%, #f2f2f2 100%); }
  .slider-dot { top: 532px; width: 14px; height: 14px; border-radius: 50%; background: #f0f0f0; border: 1px solid #bbb; }
  .slider-dot.is-current { background: var(--accent-orange); }

  /* Section title */
  .section-title { left: 0; top: 570px; width: 1150px; text-align: center; font-family: "Tinos", "Times New Roman", serif; font-weight: 400; font-size: 40px; color: var(--brand-red); line-height: 46px; }
  .section-subtitle { left: 0; top: 605px; width: 1150px; text-align: center; font-family: "Tinos", "Times New Roman", serif; font-style: italic; font-size: 31px; color: var(--text-soft); }
  .services-label { left: 18px; top: 637px; font-family: "Open Sans", Arial, sans-serif; font-size: 19px; color: var(--text-mid); }
  .services-rule { left: 15px; top: 663px; width: 1172px; height: 2px; background: var(--accent-orange); }

  /* Service cards */
  .card-rule { height: 2px; background: var(--rule-grey); width: 332px; }
  .card-title { font-size: 16px; color: var(--text-dark); }
  .card-icon { width: 88px; height: 92px; border-radius: 8px; }
  .card-text { width: 225px; font-size: 14px; line-height: 17px; color: var(--text-soft); }
  .card-link { font-size: 14px; color: var(--accent-orange); text-decoration: underline; }
</style>
</head>
<body>
  <div class="abs top-bar"></div>

  <!-- Brand -->
  <div class="abs brand-mark"></div>
  <div class="abs brand-name">Mivortal Studio, Inc.</div>
  <div class="abs brand-tagline">Website Development<br>Hosting | Content Management Systems<br>Search Engine Placement | Pay-Per-Click Advertising</div>
  <div class="abs brand-phone">855.410.2276</div>

  <!-- Account links -->
  <div class="abs account-links">
    <span><svg viewBox="0 0 13 13"><circle cx="6.5" cy="4" r="3" fill="#e8641a"/><path d="M1 13c0-4 2.5-5.5 5.5-5.5S12 9 12 13z" fill="#e8641a"/></svg>My Account</span>
    <span><svg viewBox="0 0 13 13"><rect x="2" y="1" width="9" height="11" fill="#fff" stroke="#999"/><path d="M4 5h5M4 7h5M4 9h3" stroke="#999"/></svg>Wishlist</span>
    <span><svg viewBox="0 0 13 13"><path d="M1 2h2l2 7h6l1-5H4" fill="none" stroke="#555" stroke-width="1.4"/><circle cx="6" cy="11.5" r="1.2" fill="#555"/><circle cx="10" cy="11.5" r="1.2" fill="#555"/></svg>My Cart</span>
    <span><svg viewBox="0 0 13 13"><path d="M1 7l4 4 7-9" fill="none" stroke="#e8441a" stroke-width="2"/></svg>Checkout</span>
    <span><svg viewBox="0 0 13 13"><circle cx="6.5" cy="6.5" r="6" fill="#f08a1a"/><path d="M6.5 3v4" stroke="#fff" stroke-width="1.6"/></svg>Log In</span>
  </div>
  <div class="abs cart-summary">Shopping Cart - Cart Subtotal: (<b>0</b>)</div>

  <div class="abs follow-label">Follow us on:</div>
  <div class="abs social-box" style="left:872px"></div>
  <div class="abs social-box" style="left:893px"></div>
  <div class="abs social-box" style="left:914px"></div>
  <div class="abs search-field">Search entire store here..</div>
  <div class="abs search-button">SEARCH</div>

  <!-- Navigation -->
  <div class="abs nav-rule-top"></div>
  <nav class="abs main-nav">
    <span class="is-active">HOME</span>
    <span>PORTFOLIO</span>
    <span>WEB DESIGN PRICES</span>
    <span>MARKETING PRICES</span>
    <span>GRAPHIC DESIGN PRICES</span>
    <span>WEB MAINTENANCE PRICES</span>
  </nav>
  <div class="abs nav-rule-bottom"></div>

  <!-- Hero -->
  <div class="abs hero-band"></div>
  <div class="abs hero-kicker">IF PRICE IS YOUR FIRST PRIORITY...</div>
  <div class="abs hero-headline">WE ARE FOR YOU!</div>
  <div class="abs hero-button">VIEW OUR PORTFOLIO</div>
  <div class="abs hero-devices" role="img" aria-label="Tablet and two smartphones showing the studio website on their screens"></div>
  <div class="abs slider-dot is-current" style="left:33px"></div>
  <div class="abs slider-dot" style="left:53px"></div>
  <div class="abs slider-dot" style="left:73px"></div>
  <div class="abs slider-dot" style="left:93px"></div>
  <div class="abs slider-dot" style="left:113px"></div>

  <!-- Services -->
  <h1 class="abs section-title">WEB DESIGN &amp; SUPPORT SERVICES</h1>
  <div class="abs section-subtitle">That Help You Grow Your Business!</div>
  <div class="abs services-label">SERVICES</div>
  <div class="abs services-rule"></div>

  <div class="abs card-rule" style="left:46px;top:691px"></div>
  <div class="abs card-title" style="left:44px;top:706px">Web Design</div>
  <div class="abs card-icon" style="left:36px;top:736px;background:radial-gradient(circle at 40% 40%,#5ab8f0,#0d4fa0)" role="img" aria-label="Blue globe with a paintbrush"></div>
  <div class="abs card-text" style="left:144px;top:736px">Lorem Ipsum is simply dummy text of the printing and typesetting industry.</div>
  <div class="abs card-link" style="left:144px;top:807px">read more</div>
  <div class="abs card-rule" style="left:46px;top:856px"></div>

  <div class="abs card-rule" style="left:416px;top:691px"></div>
  <div class="abs card-title" style="left:425px;top:706px">Programming Solutions</div>
  <div class="abs card-icon" style="left:430px;top:738px;background:linear-gradient(135deg,#cfe3f5,#4a86c8)" role="img" aria-label="Blueprint sheet with a pencil and ruler"></div>
  <div class="abs card-text" style="left:551px;top:742px">Lorem Ipsum is simply dummy text of the printing and typesetting industry.</div>
  <div class="abs card-link" style="left:551px;top:799px">read more</div>
  <div class="abs card-rule" style="left:416px;top:856px"></div>

  <div class="abs card-rule" style="left:811px;top:691px"></div>
  <div class="abs card-title" style="left:823px;top:706px">Signage</div>
  <div class="abs card-icon" style="left:852px;top:734px;width:60px;height:108px;background:linear-gradient(90deg,#1e1e1e,#6a6a6a)" role="img" aria-label="Freestanding black touchscreen kiosk"></div>
  <div class="abs card-text" style="left:947px;top:742px">Lorem Ipsum is simply dummy text of the printing and typesetting industry.</div>
  <div class="abs card-link" style="left:947px;top:799px">read more</div>
  <div class="abs card-rule" style="left:811px;top:856px"></div>
</body>
</html>
```